Stock Broking Firm - Web Design Project

We are looking at doing a full re-design of our home page and content page and moving the majority of our content over to DNN.

Phase 1 : Website redesign www.kpwealthdesk.com.au

The current design is too washed out, boring and has no call to action buttons.

Solution:

KP Wealthdesk is looking for a brighter/ cleaner redesign with a few stand out call to action buttons.

• Banner with logo across the top horizontally - Bright blue logo on white background similar to www.dailyledgerpress.com.au - CALL 1300 482 917 - Follow on Twitter / Facebook
• Horizontal menu bar - professional looking. - Home - About Us- Our Services - Membership - Open an Account - Become a member - Contact
• Below banner top left - large rotating banner - maybe zuvelo gallery style www.tallowhurst.com.au
• Right of rotating banner - Membership login
• Below members login - Register for Daily Market Report/ research blog - Large bright button / Name / Email / Phone / pop up??
• Below Register for daily market report - Market Indicies - RSS feed of delayed data from QNW see www.tallowhurst.com
• Below Market indicies - KP WEALTHDESK - Market Tweets ( feed from our twitter page)

Below Rotating Banner -

content area

Below content area - 4 large block buttons see www.greywickcapital.com.au ( hover over change colour)

Button 1 - EDUCATION - content - click here for more

Button 2 - Market Information and Research

Button 3 - Full service Broker - content brief - click here for more

Button 4 - Trade Commodities and Options

below buttons - small horizontal menu bar slightly different colour incl - Careers/ Partners / Legal Privacy FSG Site Map

Regards,
Colm Ashdown

Target Market(s)

35 - 65

Industry/Entity Type

Education

Requirements
Must have
• Follow brief above - large banner, call to action buttons, F.B. Twitter, Member login etc. 4 big buttons
Nice to have
• clean looking site similar to www.dailyledgerpress.com.au / not too busy. Corporate looking.
Should not have
• not too busy

```html
<!DOCTYPE html>
<html lang="en">
<head>
<meta charset="utf-8">
<title>KP Wealthdesk</title>
<link rel="stylesheet" href="https://fonts.googleapis.com/css2?family=Open+Sans:wght@400;600;700&family=Arimo:wght@400&display=swap">
<style>
:root{
  --teal:#1b6f8c;
  --teal-dark:#0d5a76;
  --teal-band:#1e7a9a;
  --cyan:#18d8ee;
  --orange:#f29a1e;
  --ink:#333;
  --link:#1a8fd6;
  --gray-top:#c4c4c4;
  --gray-bot:#9c9c9c;
  --up:#2b6a14;
  --down:#d11a1a;
}
*{margin:0;padding:0;box-sizing:border-box}
html,body{width:1200px;height:1020px;overflow:hidden;background:#fff}
body{position:relative;font-family:"Open Sans",sans-serif;color:var(--ink)}
.abs{position:absolute}
.brand{left:122px;top:20px;font-size:50px;font-weight:400;color:var(--teal);letter-spacing:-0.5px;line-height:60px}
.call{right:114px;top:30px;font-size:29px;line-height:40px;color:var(--teal-dark);font-weight:600}
.call span{color:var(--orange);font-weight:400}
.nav{left:0;top:98px;width:1200px;height:44px;background:linear-gradient(#4a4a4a,#1e1e1e);border-top:2px solid #fff;box-shadow:0 -1px 0 #222}
.nav ul{list-style:none;position:absolute;left:123px;top:12px;display:flex;gap:22px}
.nav li{color:#fff;font-size:13.5px;letter-spacing:-0.3px}
.follow{position:absolute;left:964px;top:12px;color:var(--orange);font-size:13.5px;letter-spacing:-0.3px}
.soc{position:absolute;top:8px;width:24px;height:24px;border-radius:3px;background:#3b8fc4}
.hero{left:123px;top:158px;width:674px;height:335px}
.hero-img{left:0;top:0;width:674px;height:251px;background:linear-gradient(135deg,#c24a0c,#f08a3c 45%,#9c3206 80%,#5a1c04)}
.hero-band{left:0;top:251px;width:674px;height:84px;background:linear-gradient(90deg,#2c6f86,#3f8aa6)}
.thumb{top:27px;width:68px;height:33px;background:linear-gradient(#e2e6ea,#9aa4ad)}
.thumb.on{background:linear-gradient(135deg,#b9450d,#e88840);outline:1px solid #fff}
.hero-title{left:364px;top:9px;color:#f7c21a;font-size:16px}
.hero-text{left:364px;top:33px;color:#fff;font-size:13.5px;line-height:18px;width:300px}
.tile{width:328px;height:182px;border:1px solid #8a8a8a;border-radius:3px;background:linear-gradient(var(--gray-top),var(--gray-bot));color:#fff;padding:10px 8px}
.tile.active{background:linear-gradient(var(--teal-dark),#2a85a3);border-color:#0e4e66}
.tile h3{font-size:13.5px;font-weight:700;margin-bottom:6px;letter-spacing:-0.2px}
.tile p{font-size:13.5px;line-height:18px;letter-spacing:-0.2px}
.tile a{position:absolute;left:75px;bottom:28px;color:#fff;font-size:13.5px;text-decoration:underline;letter-spacing:-0.2px}
.login{left:813px;top:157px;width:269px;height:238px;border:1px solid #c8c8c8;border-radius:3px;font-family:Arimo,sans-serif}
.login h2{position:absolute;left:8px;top:9px;font-family:"Open Sans",sans-serif;font-weight:400;font-size:17.5px;color:#222}
.lbl{left:10px;font-size:12px;color:#111}
.field{left:87px;width:170px;height:26px;border:1px solid #aaa}
.btn-login{left:87px;top:114px;width:86px;height:34px;border:1px solid #777;border-radius:3px;background:linear-gradient(#d8d8d8,#999);color:#333;font:600 14px "Open Sans",sans-serif;text-align:center;line-height:32px}
.forgot{left:190px;top:115px;font-size:12px;color:var(--link);line-height:16px}
.register{left:9px;top:158px;width:250px;height:68px;border:1px solid #d07a10;border-radius:3px;background:linear-gradient(#fdb640,#ea8a14)}
.reg-ico{left:8px;top:8px;width:50px;height:50px;background:#f4f4f4;border:1px solid #ccc}
.reg-text{left:64px;top:14px;color:#fff;font:600 17px/19px "Open Sans",sans-serif}
.reg-text small{font-size:15px;display:block;font-weight:700}
.panel{left:813px;width:268px;border:1px solid #c8c8c8;border-radius:3px;overflow:hidden}
.panel-head{height:45px;padding:12px 9px;color:#fff;font-size:15.5px}
.indices{top:410px;height:213px}
.indices .panel-head{background:var(--teal-band)}
table{width:100%;border-collapse:collapse;font-size:12px;table-layout:fixed}
th{color:var(--teal-dark);font-weight:600;font-size:13.5px;height:28px;text-align:left}
td{height:27px;border-top:1px solid #e2e2e2}
tr:nth-child(even) td{background:#f0f0f0}
td.n{color:var(--teal-dark);padding-left:10px}
td.v{color:var(--teal-dark)}
.up{color:var(--up)}.dn{color:var(--down)}
.tweets{top:638px;height:258px}
.tweets .panel-head{background:var(--cyan)}
.tweet{padding:8px 10px 0;font-size:12.3px;line-height:18px;color:#444}
.tweet a{color:var(--link);text-decoration:none}
.ago{color:#999;margin:6px 0 22px;display:flex;align-items:center;gap:8px}
.ago i{width:14px;height:10px;border-radius:50%;background:#ccc;display:inline-block}
.footer{left:0;top:923px;width:1200px;height:97px;background:linear-gradient(#2a7993,#0e4f69)}
.footer p{position:absolute;left:109px;color:#fff;font-size:13.5px;letter-spacing:-0.2px}
.footer .row1 span{margin-right:21px}
.footer .row2 small{font-size:12px}
.fsoc{top:33px;width:32px;height:32px;border-radius:50%;background:#5f94a9}
</style>
</head>
<body>
<header>
  <div class="abs brand">KP Wealthdesk</div>
  <div class="abs call"><span>Call</span> 1300 482 917</div>
</header>
<nav class="abs nav">
  <ul><li>HOME</li><li>ABOUT US</li><li>OUR SERVICES</li><li>MEMBERSHIP</li><li>OPEN AN ACCOUNT</li><li>BECOME A MEMBER</li><li>CONTACT</li></ul>
  <span class="follow">Follow us</span>
  <span class="soc" style="left:1031px" aria-label="Social profile link"></span>
  <span class="soc" style="left:1060px;background:#5cb8e6" aria-label="Social feed link"></span>
</nav>

<section class="abs hero">
  <div class="abs hero-img" role="img" aria-label="Stock exchange ticker board in orange tones"></div>
  <div class="abs hero-band">
    <div class="abs thumb" style="left:24px" role="img" aria-label="Office meeting thumbnail"></div>
    <div class="abs thumb" style="left:106px" role="img" aria-label="Team at work thumbnail"></div>
    <div class="abs thumb" style="left:189px" role="img" aria-label="Broker at desk thumbnail"></div>
    <div class="abs thumb on" style="left:271px" role="img" aria-label="Ticker board thumbnail"></div>
    <div class="abs hero-title">Lorem ipsum dolor sit amet</div>
    <div class="abs hero-text">Etiam tristique ipsum in nulla facilisis tristique. Nulla vehicula tortor sed odio porta aliquet.</div>
  </div>
</section>

<div class="abs tile active" style="left:121px;top:512px">
  <h3>Education</h3>
  <p>Massa aliquet adipiscing. Sed dignissim aliquam vestibulum. Cras non nisl at neque ultrices pharetra. Ut justo lorem, venenatis non fermentum</p>
  <a>Click Here to Learn More</a>
</div>
<div class="abs tile" style="left:470px;top:512px">
  <h3>Market Information and Research</h3>
  <p>Fusce eu augue sed massa aliquet adipiscing. Sed dignissim aliquam vestibulum. Cras non nisl at neque ultrices pharetra. Ut justo lorem, venenatis non fermentum</p>
  <a>Click Here to Learn More</a>
</div>
<div class="abs tile" style="left:121px;top:713px">
  <h3>Full service Broker</h3>
  <p>Cras augue sed massa aliquet adipiscing. Sed dignissim aliquam vestibulum. Cras non nisl at neque ultrices pharetra. Ut justo lorem, venenatis non fermentum</p>
  <a>Click Here to Learn More</a>
</div>
<div class="abs tile" style="left:470px;top:713px">
  <h3>Trade Commodities and Options</h3>
  <p>Ut lastok ke Fusce eu augue sed massa aliquet adipiscing. Sed dignissim aliquam vestibulum. Cras non nisl at neque ultrices pharetra. Ut justo lorem, venenatis non fermentum</p>
  <a>Click Here to Learn More</a>
</div>

<aside class="abs login">
  <h2>MEMBERSHIP LOGIN</h2>
  <span class="abs lbl" style="top:52px">User Name</span>
  <span class="abs field" style="top:45px"></span>
  <span class="abs lbl" style="top:82px">Password</span>
  <span class="abs field" style="top:78px"></span>
  <div class="abs btn-login">LOGIN</div>
  <div class="abs forgot">Forgot<br>Password?</div>
  <div class="abs register">
    <div class="abs reg-ico">
      <svg width="50" height="50" viewBox="0 0 50 50"><rect x="10" y="22" width="8" height="20" fill="#2a9ad8"/><rect x="21" y="12" width="8" height="30" fill="#e23a2a"/><rect x="32" y="26" width="8" height="16" fill="#3fae3a"/><rect x="8" y="42" width="34" height="2" fill="#666"/></svg>
    </div>
    <div class="abs reg-text">REGISTER FOR<small>DAILY MARKET REPORT</small></div>
  </div>
</aside>

<aside class="abs panel indices">
  <div class="panel-head">Market Indices</div>
  <table>
    <colgroup><col style="width:70px"><col style="width:72px"><col style="width:64px"><col></colgroup>
    <tr><th style="padding-left:10px">Name</th><th>Value</th><th>+/-</th><th>%+/-</th></tr>
    <tr><td class="n">All Shares</td><td class="v">4,513.82</td><td class="up">+41.22</td><td class="up">+0.92</td></tr>
    <tr><td class="n">KX200</td><td class="v">4,494.38</td><td class="up">+41.98</td><td class="up">+0.94</td></tr>
    <tr><td class="n">Indu30</td><td class="v">13,610.15</td><td class="up">+34.79</td><td class="up">+0.26</td></tr>
    <tr><td class="n">HKBlue</td><td class="v">21,012.38</td><td class="up">+104.43</td><td class="up">+0.50</td></tr>
    <tr><td class="n">TECHX</td><td class="v">3,136.19</td><td class="dn">-13.27</td><td class="dn">-0.42</td></tr>
  </table>
</aside>

<aside class="abs panel tweets">
  <div class="panel-head">KP Wealthdesk - Market Tweets</div>
  <div class="tweet">Nam odio diam, pellentesque id pharetra sit amet, faucibus sed ante @ <a>nora vell</a>: PHARETRA SIT AMET <a>http://kpw.lk/mR4q</a>
    <div class="ago"><i></i>about 2 hours ago</div>
    Nam odio diam, pellentesque id pharetra sit amet, faucibus sed ante @ <a>Ida Rusk</a>: PHARETRA SIT AMET <a>http://kpw.lk/mR4q</a>
    <div class="ago"><i></i>about 4 hours ago</div>
  </div>
</aside>

<footer class="abs footer">
  <p class="row1" style="top:28px"><span>Home</span><span>About Us</span><span>Our Services</span><span>Membership</span><span>Open an Account</span><span>Become a member</span><span>Contact</span></p>
  <p class="row2" style="top:52px">Careers&nbsp; |&nbsp; Partners&nbsp; |&nbsp; Legal&nbsp; |&nbsp; Privacy&nbsp; |&nbsp; FSG Site Map | <small>© 2012 KP Wealthdesk. All rights reserved</small></p>
  <span class="abs fsoc" style="left:1007px" aria-label="Social feed link"></span>
  <span class="abs fsoc" style="left:1057px" aria-label="Social profile link"></span>
</footer>
</body>
</html>
```